Business Card and Stationery for Bellwick Home Services
Bellwick Home Services
Professional
R. Owen Tallis
President/CEO
4187 Marrow Creek Lane,
Suite K
Baton Rouge LA 70342
rowentallis@bellwickhomeservices.biz
www.bellwickhomeservice.biz
Commercial License # 53419 Residential LIcense # 21398
The color formula for the orange is:
C=0 M=74 Y=100 K=0
We take care of all of your home needs.
Plumbing, Heating and AIr, Electrical, Remodeling, Roofing, New Construction, Insurance Damage Repairs, Fire Restoration, if its in you home, we can service it or take care of it for you!!!
THESE ARE JUST IDEAS, want to use the back for information, etc.......maybe a light watermark on the back, using part of the logo, showing under the lettering. Would like the back to be the orange color

```html
<!DOCTYPE html>
<html lang="en">
<head>
<meta charset="utf-8">
<title>Bellwick Home Services – Business Card</title>
<link rel="stylesheet" href="https://fonts.googleapis.com/css2?family=Roboto:wght@400;700&display=swap">
<style>
  :root {
    --orange: #f26522;
    --grey: #9a9a9a;
    --ink: #3a3a3a;
    --white: #ffffff;
    --backdrop: #ececec;
  }
  * { margin: 0; padding: 0; box-sizing: border-box; }
  html, body { width: 1200px; height: 914px; overflow: hidden; }
  body {
    background: var(--backdrop);
    font-family: "Roboto", Arial, sans-serif;
    position: relative;
  }
  .business-card {
    position: absolute;
    left: 80px; top: 160px;
    width: 1040px; height: 594px;
    background: var(--white);
    overflow: hidden;
    box-shadow: 0 6px 24px rgba(0,0,0,.18);
  }
  .card-swoosh { position: absolute; inset: 0; width: 1040px; height: 594px; }
  .brand {
    position: absolute; left: 70px; top: 48px;
  }
  .brand-square {
    width: 112px; height: 112px; border-radius: 18px;
    background: var(--orange);
  }
  .brand-name {
    margin-top: 14px;
    font-weight: 700; font-size: 22px; color: var(--ink);
  }
  .person { position: absolute; left: 70px; top: 222px; }
  .person-name { color: var(--orange); font-size: 27px; font-weight: 400; }
  .person-title { color: var(--ink); font-size: 19px; margin-top: 6px; }
  .street-address {
    position: absolute; left: 40px; top: 432px;
    color: var(--white); font-size: 23px;
  }
  .contact-list {
    position: absolute; left: 660px; top: 378px;
    list-style: none; color: var(--white); font-size: 15px;
  }
  .contact-list li {
    display: flex; align-items: center; gap: 10px;
    height: 26px;
  }
  .contact-icon { width: 16px; height: 16px; flex: none; }
</style>
</head>
<body>
  <main class="business-card">
    <svg class="card-swoosh" viewBox="0 0 1040 594" aria-hidden="true">
      <path d="M0,296 C300,372 700,362 1040,232 L1040,252 C700,382 300,392 0,314 Z" fill="var(--grey)"/>
      <path d="M0,320 C300,398 700,388 1040,258 L1040,594 L0,594 Z" fill="var(--orange)"/>
    </svg>

    <div class="brand">
      <div class="brand-square"></div>
      <div class="brand-name">Bellwick Home Services</div>
    </div>

    <div class="person">
      <div class="person-name">R. Owen Tallis</div>
      <div class="person-title">President/CEO</div>
    </div>

    <p class="street-address">4187 Marrow Creek Lane, Suite K Baton Rouge LA 70342</p>

    <ul class="contact-list">
      <li>
        <svg class="contact-icon" viewBox="0 0 16 16"><circle cx="8" cy="8" r="8" fill="var(--white)"/><path d="M8 3.5a3 3 0 0 0-3 3c0 2.2 3 6 3 6s3-3.8 3-6a3 3 0 0 0-3-3z" fill="var(--orange)"/></svg>
        4187 Marrow Creek Lane, Suite K
      </li>
      <li><span class="contact-icon"></span>Baton Rouge LA 70342</li>
      <li>
        <svg class="contact-icon" viewBox="0 0 16 16"><circle cx="8" cy="8" r="8" fill="var(--white)"/><path d="M5 4l2 0 1 2.5-1.2 1a5 5 0 0 0 2.7 2.7l1-1.2 2.5 1v2a1 1 0 0 1-1 1A8 8 0 0 1 4 5a1 1 0 0 1 1-1z" fill="var(--orange)"/></svg>
        225-555-0147
      </li>
      <li>
        <svg class="contact-icon" viewBox="0 0 16 16"><circle cx="8" cy="8" r="8" fill="var(--white)"/><rect x="5.5" y="3.5" width="5" height="9" rx="1" fill="var(--orange)"/></svg>
        225-555-0182
      </li>
      <li>
        <svg class="contact-icon" viewBox="0 0 16 16"><circle cx="8" cy="8" r="8" fill="var(--white)"/><rect x="4" y="6" width="8" height="5" fill="var(--orange)"/></svg>
        225-555-0193
      </li>
      <li>
        <svg class="contact-icon" viewBox="0 0 16 16"><circle cx="8" cy="8" r="8" fill="var(--white)"/><rect x="4" y="5" width="8" height="6" fill="var(--orange)"/><path d="M4 5l4 3.5 4-3.5" stroke="var(--white)" fill="none"/></svg>
        rowentallis@bellwickhomeservices.biz
      </li>
      <li>
        <svg class="contact-icon" viewBox="0 0 16 16"><circle cx="8" cy="8" r="8" fill="var(--white)"/><circle cx="8" cy="8" r="4" fill="none" stroke="var(--orange)" stroke-width="1.4"/><path d="M4 8h8" stroke="var(--orange)" stroke-width="1.2"/></svg>
        www.bellwickhomeservice.biz
      </li>
    </ul>
  </main>
</body>
</html>
```